Letterhead design for business

Looking for an attractive and professional letterhead that uses the logo that is attached below.

Target Market(s)

Potential bankruptcy clients.

Industry/Entity Type

Legal

Colors

Designer to choose colors to be used in the design.

Requirements
Must have
• Address for locations, phone number, and website address.
• Addresses are on website ferncoveadvice.example. Use following phone number (for tracking purposes): 555-013-8274

```html
<!DOCTYPE html>
<html lang="en">
<head>
<meta charset="utf-8">
<title>Ferncove Law Group Letterhead</title>
<link rel="stylesheet" href="https://fonts.googleapis.com/css2?family=Arimo:wght@700&family=PT+Sans:wght@400;700&display=swap">
<style>
  :root {
    --backdrop: #e4e5e6;
    --paper: #fbfbfb;
    --charcoal: #3d3d3f;
    --fern: #7dbb74;
    --fern-faint: #e3efe1;
    --ink: #2b2b2b;
    --muted: #555;
  }
  * { box-sizing: border-box; margin: 0; padding: 0; }
  html, body { width: 1200px; height: 945px; overflow: hidden; background: var(--backdrop); }
  .letterhead {
    position: absolute; left: 260px; top: 24px;
    width: 680px; height: 897px;
    background: var(--paper);
    box-shadow: 0 4px 18px rgba(0,0,0,.12);
    overflow: hidden;
    font-family: "PT Sans", sans-serif;
    color: var(--ink);
  }
  .side-bands { position: absolute; left: 0; top: 0; }
  .brand {
    position: absolute; left: 96px; top: 46px;
    display: flex; align-items: center; gap: 10px;
  }
  .brand-dot { width: 30px; height: 30px; border-radius: 50%; background: var(--fern); }
  .brand-rule { width: 1px; height: 40px; background: var(--fern); }
  .brand-name { font-size: 20px; font-weight: 700; color: var(--fern); line-height: 1; }
  .brand-tag { font-size: 8px; color: var(--fern); margin-top: 4px; letter-spacing: .3px; }
  .letter { position: absolute; left: 110px; top: 200px; width: 500px; }
  .salutation { font-family: "Arimo", sans-serif; font-weight: 700; font-size: 15px; margin-bottom: 14px; }
  .letter p { font-size: 12.5px; line-height: 1.38; color: var(--muted); margin-bottom: 14px; text-indent: 40px; }
  .letter p.lead { text-indent: 0; }
  .signature {
    width: 150px; height: 44px; margin-top: 26px; margin-left: 30px;
    background: linear-gradient(90deg, #d8d8d8, #efefef);
    border-radius: 4px;
  }
  .seal-mark {
    position: absolute; right: 40px; top: 620px;
    width: 74px; height: 74px; border-radius: 50%; background: var(--fern-faint);
  }
  .contact { position: absolute; left: 86px; bottom: 34px; list-style: none; }
  .contact li { display: flex; align-items: center; gap: 7px; font-size: 10.5px; color: var(--ink); line-height: 1.35; }
  .contact svg { flex: none; }
</style>
</head>
<body>
<main class="letterhead">
  <svg class="side-bands" width="80" height="897" viewBox="0 0 80 897" aria-hidden="true">
    <polygon points="0,0 30,0 30,897 0,897" fill="var(--charcoal)"/>
    <polygon points="36,0 58,0 40,897 36,897" fill="var(--fern)"/>
  </svg>

  <header class="brand">
    <span class="brand-dot"></span>
    <span class="brand-rule"></span>
    <div>
      <div class="brand-name">Ferncove Law Group</div>
      <div class="brand-tag">by Attorney R. Calloway</div>
    </div>
  </header>

  <section class="letter">
    <h1 class="salutation">Dear Mr. John,</h1>
    <p class="lead">Lorem Ipsum is simply dummy text of the printing and typesetting industry. Lorem Ipsum has been the industry's standard dummy text ever since the 1500s, when an unknown printer took a galley of type and scrambled it to make a type specimen book. It has survived not only five centuries, but also the leap into electronic typesetting, remaining essentially unchanged.</p>
    <p>The standard chunk of Lorem Ipsum used since the 1500s is reproduced below for those interested. Sections 1.10.32 and 1.10.33 from "de Finibus Bonorum et Malorum" by Cicero are also reproduced in their exact original form, accompanied by English versions from the 1914 translation by H. Rackham</p>
    <p>Lorem Ipsum is simply dummy text of the printing and typesetting industry. Lorem Ipsum has been the industry's standard dummy text ever since the 1500s, when an unknown printer took a galley of type and scrambled it to make a type specimen book. It has survived not only five centuries, but also the leap into electronic typesetting, remaining essentially unchanged. It was popularised in the</p>
    <p>The standard chunk of Lorem Ipsum used since the 1500s is reproduced below for those interested. Sections 1.10.32 and 1.10.33 from "de Finibus Bonorum et Malorum" by Cicero are also reproduced in their exact original form, accompanied by English versions from the 1914 translation by H. Rackham</p>
    <div class="signature" role="img" aria-label="Handwritten signature of the attorney"></div>
  </section>

  <div class="seal-mark" aria-hidden="true"></div>

  <ul class="contact">
    <li>
      <svg width="11" height="11" viewBox="0 0 11 11" aria-hidden="true"><rect width="11" height="11" fill="var(--fern)"/><path d="M3 2.5l1.2 0 .6 1.6-.8.6a4 4 0 0 0 2.3 2.3l.6-.8 1.6.6 0 1.2c-3 .3-5.8-2.5-5.5-5.5z" fill="#fff"/></svg>
      555-013-8274
    </li>
    <li>
      <svg width="11" height="11" viewBox="0 0 11 11" aria-hidden="true"><rect width="11" height="11" fill="var(--fern)"/><circle cx="5.5" cy="5.5" r="3" fill="none" stroke="#fff" stroke-width=".8"/><path d="M2.5 5.5h6M5.5 2.5c-1.5 1.8-1.5 4.2 0 6M5.5 2.5c1.5 1.8 1.5 4.2 0 6" fill="none" stroke="#fff" stroke-width=".6"/></svg>
      www.ferncoveadvice.example
    </li>
    <li>
      <svg width="11" height="11" viewBox="0 0 11 11" aria-hidden="true"><rect width="11" height="11" fill="var(--fern)"/><path d="M5.5 2a2.2 2.2 0 0 1 2.2 2.2c0 1.7-2.2 4.3-2.2 4.3S3.3 5.9 3.3 4.2A2.2 2.2 0 0 1 5.5 2z" fill="#fff"/><circle cx="5.5" cy="4.2" r=".8" fill="var(--fern)"/></svg>
      48 Linden Row, Suite #210 Marlow, Georgia 30999
    </li>
    <li>
      <svg width="11" height="11" viewBox="0 0 11 11" aria-hidden="true"><rect width="11" height="11" fill="var(--fern)"/><path d="M5.5 2a2.2 2.2 0 0 1 2.2 2.2c0 1.7-2.2 4.3-2.2 4.3S3.3 5.9 3.3 4.2A2.2 2.2 0 0 1 5.5 2z" fill="#fff"/><circle cx="5.5" cy="4.2" r=".8" fill="var(--fern)"/></svg>
      915 Orchard Ave. Fernhill, Georgia 30998
    </li>
  </ul>
</main>
</body>
</html>
```